Business card design for a dynamic IT consulting company

We need a business card design for a young firm, specialized in the Telecommunications/Consulting industry. The name of the company is Brask and Partners Business Consulting Ltd. (Short name: Brask and Partnes)
Brask = solve read reverse, so we aim to be uncomplicated and solution-oriented. The small pipe in our logo is also related to the word solve. So we need a new business card design, which is simple, eye catching and something non traditional (I would probably prefer a square shaped design rather than a rectangle, but open for suggestions). Attached our logo.

Target Market(s)

Usually our customers are Tier1 Telecoms providers (Q-Linkra, Parnexo, etc) and their executives.

Industry/Entity Type

Business

Contact Information for Business Card

Name: Gergely Halmindo
Email: g.halmindo@braskpartnera.hu
Web: www.braskpartnera.hu
Mobile: +36 30 555 0192
Title: Managing Director

Optional:
Company name: Brask and Partners Ltd.
Address: 1047 Budapest, Ravaszi str. 17/B, Hungary

Font styles to use
Other font styles liked:
• helveticaneue_medium, Prime Regular are used now.

Colors

Designer to choose colors to be used in the design.

Requirements
Must have
• I would like to have a 2 sided design.
Nice to have
• I thought if we make the logo a bit bigger (without the company name), that could go to the back with the company name below. I though, if the pipe in the logo is somehow touchable on the business card, would be nice and unique.

```html
<!DOCTYPE html>
<html lang="en">
<head>
<meta charset="utf-8">
<title>Brask and Partners – Business Cards</title>
<link rel="stylesheet" href="https://fonts.googleapis.com/css2?family=Open+Sans:wght@400;600;700&display=swap">
<style>
  :root {
    --backdrop: #7f8083;
    --card: #0b0b0c;
    --band: #e6e6e7;
    --ink-dark: #141414;
    --ink-muted: #8c8c8e;
    --ink-light: #a2a2a4;
    --brand-white: #f2f2f2;
    --accent: #2fb8d6;
  }
  * { margin: 0; padding: 0; box-sizing: border-box; }
  html, body {
    width: 1200px; height: 898px; overflow: hidden;
    background: var(--backdrop);
    font-family: "Open Sans", Arial, sans-serif;
  }
  .canvas { position: relative; width: 1200px; height: 898px; }

  .card {
    position: absolute; top: 207px;
    width: 387px; height: 387px;
    background: var(--card);
    border-radius: 18px;
    box-shadow: 6px 8px 10px rgba(0,0,0,0.35);
    overflow: hidden;
  }
  .card--front { left: 157px; }
  .card--back { left: 643px; }

  .brand {
    position: absolute; left: 24px; top: 42px;
    display: flex; align-items: center; gap: 14px;
  }
  .brand__square { width: 28px; height: 28px; background: var(--accent); }
  .brand__name {
    color: var(--brand-white);
    font-weight: 400; font-size: 32px; letter-spacing: 0.2px;
    line-height: 1;
  }

  .band {
    position: absolute; left: 3px; right: 3px; top: 235px; height: 47px;
    background: var(--band);
    display: flex; flex-direction: column; align-items: center; justify-content: center;
  }
  .person__name {
    color: var(--ink-dark); font-weight: 600; font-size: 22px;
    letter-spacing: 1px; line-height: 1.05;
  }
  .person__title {
    color: var(--ink-muted); font-size: 12px; letter-spacing: 1.6px; line-height: 1.2;
  }
  .company__name {
    color: var(--ink-dark); font-weight: 600; font-size: 20px; letter-spacing: 0.8px;
  }

  .details {
    position: absolute; left: 0; right: 0;
    text-align: center; color: var(--ink-light);
    font-size: 18.5px; line-height: 23px;
  }
  .card--front .details { top: 296px; }
  .card--back .details { top: 305px; line-height: 24px; }
</style>
</head>
<body>
<main class="canvas">
  <section class="card card--front" aria-label="Card front">
    <div class="brand">
      <span class="brand__square"></span>
      <span class="brand__name">Brask &amp; Partners</span>
    </div>
    <div class="band">
      <p class="person__name">Gergely Halmindo</p>
      <p class="person__title">Managing Director</p>
    </div>
    <div class="details">
      <p>g.halmindo@braskpartnera.hu</p>
      <p>www.braskpartnera.hu</p>
      <p>+36 30 555 0192</p>
    </div>
  </section>

  <section class="card card--back" aria-label="Card back">
    <div class="brand">
      <span class="brand__square"></span>
      <span class="brand__name">Brask &amp; Partners</span>
    </div>
    <div class="band">
      <p class="company__name">BRASK AND PARTNERS LTD.</p>
    </div>
    <div class="details">
      <p>1047 Budapest, Ravaszi str.</p>
      <p>17/B, Hungary</p>
    </div>
  </section>
</main>
</body>
</html>
```